Brochure Design Project - Innovative Service for Pharma Industry

Our start up is based in Germany, near Munich and we provide an innovative Service for the pharma industry. We develop product trainings and general trainings online. The adressed audience for these trainings are pharmacies and medics. The parma industry could increase the number of trainings, while saving money (incl a success guarantee). Our (not yet finnished) corporate page can be reviewed here: www.brevoloq.biz, our 'product & service' page is www.kestrumlearn.com. The color code should be leaned towards the corporate page.

The brochure should be send to decision makers in the pharma industry and rise the interest in innovative service. Seriousity should meet modern & clear design.Something eye cathing on the front page might be required.

Target Market(s)

Usually more conservative decision makers within the pharma industry

Industry/Entity Type

Industry

Requirements
Must have
• Conceptional design for an brochure (Din A4 size) of approx 6-8 pages, that capture the key messages (exact content would be filled / provided from us)
Nice to have
• Implementing some of the pics / phrases on the home page www.brevolq.biz could be maybe nice. How about a personal statement from the founder combined with a pic(pic attached)? Both is no must....

```html
<!DOCTYPE html>
<html lang="de">
<head>
<meta charset="utf-8">
<title>Brevoloq – About Us</title>
<link rel="stylesheet" href="https://fonts.googleapis.com/css2?family=Didact+Gothic&display=swap">
<style>
  :root {
    --page-bg: #ffffff;
    --accent: #e8502a;
    --text: #5a5a5a;
    --rule: #bdbdbd;
    --photo-dark: #2a2226;
    --photo-skin: #e7b89a;
    --photo-light: #f3d3bd;
  }
  * { margin: 0; padding: 0; box-sizing: border-box; }
  html, body {
    width: 1200px;
    height: 908px;
    overflow: hidden;
    background: var(--page-bg);
  }
  .page {
    position: relative;
    width: 1200px;
    height: 908px;
    font-family: "Didact Gothic", "Century Gothic", sans-serif;
    color: var(--text);
  }
  .hero-photo {
    position: absolute;
    left: 0;
    top: 0;
  }
  .rule-vertical {
    position: absolute;
    left: 63px;
    top: 397px;
    width: 1px;
    height: 388px;
    background: var(--rule);
  }
  .rule-horizontal {
    position: absolute;
    left: 32px;
    top: 479px;
    width: 630px;
    height: 1px;
    background: var(--rule);
  }
  .brand {
    position: absolute;
    right: 50px;
    top: 44px;
    width: 220px;
    height: 210px;
  }
  .brand-dot {
    position: absolute;
    left: 70px;
    top: 20px;
    width: 100px;
    height: 100px;
    border-radius: 50%;
    background: var(--accent);
  }
  .brand-name {
    position: absolute;
    right: 0;
    top: 145px;
    font-size: 50px;
    line-height: 1;
    color: var(--accent);
    letter-spacing: 0.5px;
  }
  .about {
    position: absolute;
    left: 98px;
    top: 505px;
    width: 960px;
  }
  .about-title {
    font-size: 37px;
    font-weight: 400;
    color: var(--accent);
    line-height: 44px;
    margin-bottom: 20px;
  }
  .about-text {
    font-size: 19px;
    line-height: 24.5px;
    margin-bottom: 24px;
  }
  .page-number {
    position: absolute;
    left: 1132px;
    top: 836px;
    font-size: 19px;
    color: var(--text);
  }
</style>
</head>
<body>
  <main class="page">
    <svg class="hero-photo" width="600" height="440" viewBox="0 0 600 440" role="img" aria-label="Portrait photo of a young woman framing her view with both hands, cropped to a circle">
      <defs>
        <clipPath id="hero-crop">
          <circle cx="300" cy="260" r="238"/>
        </clipPath>
        <radialGradient id="hero-tones" cx="0.5" cy="0.55" r="0.65">
          <stop offset="0" stop-color="var(--photo-skin)"/>
          <stop offset="0.55" stop-color="var(--photo-light)"/>
          <stop offset="1" stop-color="var(--photo-skin)"/>
        </radialGradient>
        <linearGradient id="hero-top" x1="0" y1="0" x2="0" y2="1">
          <stop offset="0" stop-color="var(--photo-dark)" stop-opacity="0.85"/>
          <stop offset="0.45" stop-color="var(--photo-dark)" stop-opacity="0"/>
        </linearGradient>
      </defs>
      <g clip-path="url(#hero-crop)">
        <rect x="0" y="0" width="600" height="438" fill="url(#hero-tones)"/>
        <rect x="0" y="0" width="600" height="438" fill="url(#hero-top)"/>
      </g>
    </svg>

    <div class="rule-vertical"></div>
    <div class="rule-horizontal"></div>

    <div class="brand">
      <span class="brand-dot"></span>
      <span class="brand-name">brevoloq</span>
    </div>

    <section class="about">
      <h1 class="about-title">About Us</h1>
      <p class="about-text">
        Das Unternehmen wurde 2011 bei München gegründet um unter Ausnutzung neuster<br>
        CLOUD Technologien modernste E-Learning Lösungen anzubieten. Hierbei zielen wir<br>
        auf vertikale Märkte von erklärungsbedürftigen Produkten. Gemeinsam mit unseren<br>
        Kunden neuste Konzepte zu erarbeiten und Plattformen zu betreiben ist unsere Aufgabe.<br>
        Hierbei berücksichtigen wir die individuellen Bedürfnisse unserer Kunden.
      </p>
      <p class="about-text">
        Die erfolgreiche Erstimplementierung einer industrieweiten E-Learning Platform dient<br>
        als Grundlage um den Service auf andere Länder oder Zielgruppen auszuweiten.<br>
        Die Pharmaindustrie ist der primäre Zielmarkt für unser Unternehmen.
      </p>
    </section>

    <div class="page-number">4</div>
  </main>
</body>
</html>
```